New Company Business Card Design

I have a new company logo and I want a new business card design. I dont know if the logo file i attached is in the correct format or quality. We are a New York City Specialty construction Firm specializing in high risk out of the box projects. I want a simple and classy business card that people will his card is as crisp as the work his company does.

Target Market(s)

Clients in the heavy construction industry in New York City

Industry/Entity Type

Construction Company

Contact Information for Business Card

Simple Classy - DIFFERENT

Font styles to use
Other font styles liked:
• Mach the logo font in some way

Colors

Designer to choose colors to be used in the design.

Requirements
Must have
• Uniqueness
Nice to have
• Nothing particular - Just different and classy - Timeless
Should not have
• Goofy Shit or Gimmicky shit

```html
<!DOCTYPE html>
<html lang="en">
<head>
<meta charset="utf-8">
<title>Karrow Builders, Inc. — Business Card</title>
<link href="https://fonts.googleapis.com/css2?family=Montserrat:wght@500;700&family=Quicksand:wght@400;500&display=swap" rel="stylesheet">
<style>
  :root{
    --ink:#231f20;
    --ink-soft:#2e2a2b;
    --paper:#ffffff;
    --blue:#1b7fd1;
    --blue-deep:#0f4f95;
    --stage:#3a3a3c;
    --text-dark:#2b2b2b;
  }
  *{box-sizing:border-box;margin:0;padding:0}
  html,body{width:1200px;height:929px;overflow:hidden}
  body{background:var(--stage);display:flex;align-items:center;justify-content:center;gap:40px;font-family:"Quicksand",sans-serif}
  .card{width:560px;height:320px;position:relative;overflow:hidden;box-shadow:0 14px 30px rgba(0,0,0,.45)}
  .brand{font-family:"Montserrat",sans-serif;font-weight:700;color:var(--blue);text-align:center;line-height:1.05;letter-spacing:.06em;display:flex;align-items:center;gap:10px;justify-content:center}
  .brand-mark{width:14px;height:14px;background:var(--blue)}
  .brand-name{font-size:30px}
  .brand-name small{display:block;font-size:13px;letter-spacing:.32em;margin-top:4px}

  /* back */
  .card-back{background:var(--ink)}
  .back-decor{position:absolute;left:80px;top:0;width:400px;height:320px;background:linear-gradient(160deg,rgba(255,255,255,.035),rgba(255,255,255,0) 70%)}
  .edge-tab{position:absolute;width:14px;height:60px;background:linear-gradient(90deg,var(--blue-deep),var(--blue))}
  .edge-tab.left{left:0;top:190px}
  .edge-tab.right{right:0;top:50px}
  .card-back .brand{position:absolute;left:0;right:0;top:100px}
  .address{position:absolute;left:0;right:0;bottom:50px;text-align:center;color:#fff;font-size:15px;font-weight:500;letter-spacing:.02em}

  /* front */
  .card-front{background:var(--paper)}
  .card-front .brand{position:absolute;left:0;right:0;top:44px}
  .person{position:absolute;left:0;right:0;top:140px;text-align:center}
  .person-name{font-family:"Montserrat",sans-serif;font-weight:700;font-size:20px;color:var(--text-dark);letter-spacing:.03em}
  .person-role{font-size:15px;color:var(--blue);margin-top:2px}
  .person-rule{width:120px;height:2px;background:var(--blue);margin:6px auto 0}
  .contact-band{position:absolute;left:0;right:0;bottom:0;height:82px;background:var(--ink)}
  .contacts{position:absolute;left:0;right:0;top:206px;display:flex;justify-content:space-around;padding:0 20px}
  .contact{display:flex;flex-direction:column;align-items:center;gap:8px;font-size:14px;color:var(--text-dark)}
  .contact-icon{width:30px;height:30px;border-radius:50%;background:var(--blue);border:2px solid #fff;box-shadow:0 0 0 1px var(--blue-deep);display:flex;align-items:center;justify-content:center;margin-top:4px}
</style>
</head>
<body>
  <section class="card card-back">
    <div class="back-decor" role="img" aria-label="Faint steel tower structure in the background"></div>
    <span class="edge-tab left"></span>
    <span class="edge-tab right"></span>
    <div class="brand">
      <span class="brand-mark"></span>
      <span class="brand-name">KARROW<small>BUILDERS, INC.</small></span>
    </div>
    <p class="address">48 Ridge Lane, Suite B, Leeds, UK 20417B</p>
  </section>

  <section class="card card-front">
    <div class="brand">
      <span class="brand-mark"></span>
      <span class="brand-name">KARROW<small>BUILDERS, INC.</small></span>
    </div>
    <div class="person">
      <p class="person-name">DANA REYES</p>
      <p class="person-role">Founder &amp; CEO</p>
      <div class="person-rule"></div>
    </div>
    <div class="contact-band"></div>
    <div class="contacts">
      <div class="contact">
        <span>555 014 2290</span>
        <span class="contact-icon">
          <svg width="14" height="14" viewBox="0 0 24 24" fill="#fff"><path d="M6.6 10.8a15 15 0 0 0 6.6 6.6l2.2-2.2c.3-.3.7-.4 1-.2 1.1.4 2.3.6 3.6.6.6 0 1 .4 1 1V20c0 .6-.4 1-1 1C10.6 21 3 13.4 3 4c0-.6.4-1 1-1h3.5c.6 0 1 .4 1 1 0 1.3.2 2.5.6 3.6.1.3 0 .7-.2 1z"/></svg>
        </span>
      </div>
      <div class="contact">
        <span>info@karrowbuilders.com</span>
        <span class="contact-icon">
          <svg width="14" height="14" viewBox="0 0 24 24" fill="none" stroke="#fff" stroke-width="2"><rect x="3" y="5" width="18" height="14" rx="1"/><path d="M3 6l9 7 9-7"/></svg>
        </span>
      </div>
      <div class="contact">
        <span>karrowbuilders.com</span>
        <span class="contact-icon">
          <svg width="14" height="14" viewBox="0 0 24 24" fill="none" stroke="#fff" stroke-width="1.8"><circle cx="12" cy="12" r="9"/><path d="M3 12h18M12 3c3 3 3 15 0 18M12 3c-3 3-3 15 0 18"/></svg>
        </span>
      </div>
    </div>
  </section>
</body>
</html>
```